finlo-welt.de
Zielgruppe
Alle die kein Geld haben :-)
Aufgabenstellung
Unter finlo-welt.de sollen Informationen rund um Kredite, Kreditkarten, Bonvia usw. entstehen. Diese werden dann unter Subdomains wir konto.finlo-welt.de oder kreditkarte.finlo-welt.de laufen. Die Domain finlo-welt.de soll die Hauptdomain werden wofür ein Logo und ein Layout benötigt wird. Auf den einzelnen Seiten sollen später Reporte verkauft werden und relativ viel mit Plunko Werbung gearbeitet werden. Hier ein paar Beipspiele www.zahlwerk-mohnel.biz, www.lumvesta88.de, www.tanne-blau-heft.de, www.nordlicht-mappe-brief.de
Die genannten Seiten sind keine Meisterleistung in Design und sollen nur in etwa Inhalte und die Einbindung von Plunko Adbox wieder geben. Menüpunkte sind immer gleich und werden sein mit den Untertiteln wie bei www.zahlwerk-mohnel.biz.

```html
<!DOCTYPE html>
<html lang="de">
<head>
<meta charset="utf-8">
<title>finlo-welt.de</title>
<link rel="stylesheet" href="https://fonts.googleapis.com/css2?family=Arimo:wght@400;700&family=Noto+Sans:wght@400;700&display=swap">
<style>
  :root {
    --bg: #ffffff;
    --nav-blue: #1f9bd7;
    --ad-title: #222222;
    --ad-text: #5a5a5a;
    --ad-url: #333333;
    --divider: #eeeeee;
    --arrow-box: #222222;
    --photo-light: #e9e9ea;
    --photo-dark: #2b2d33;
  }
  * { margin: 0; padding: 0; box-sizing: border-box; }
  html, body { width: 1200px; height: 711px; overflow: hidden; background: var(--bg); }
  .page { position: relative; width: 1200px; height: 711px; }

  .main-nav {
    position: absolute; left: 50px; top: 159px;
    display: flex; align-items: center; gap: 10px;
    font-family: "Arimo", Arial, sans-serif; font-weight: 700; font-size: 16px;
    letter-spacing: 0.3px; color: var(--nav-blue);
  }
  .main-nav .home-icon { width: 22px; height: 22px; display: block; }
  .main-nav .sep { font-weight: 400; }
  .main-nav a { color: inherit; text-decoration: none; }

  .brand {
    position: absolute; left: 822px; top: 122px;
    font-family: "Arimo", Arial, sans-serif; font-weight: 700; font-size: 60px;
    letter-spacing: -1px; color: var(--nav-blue); line-height: 1;
  }

  .ad-column {
    position: absolute; top: 228px; height: 451px; overflow: hidden;
    font-family: "Noto Sans", Verdana, sans-serif;
  }
  .ad-column.left { left: 52px; width: 204px; border-right: 8px solid var(--divider); }
  .ad-column.right { left: 300px; width: 202px; border-right: 8px solid var(--divider); }

  .ad-head {
    display: flex; justify-content: space-between; align-items: center;
    height: 24px; padding-right: 10px; margin-bottom: 24px;
    font-size: 14px; color: #333;
  }
  .ad-head .source { font-size: 16px; letter-spacing: -0.3px; }
  .ad-head .source small { font-size: 12px; }
  .ad-head .source.house { font-family: "Arimo", Arial, sans-serif; font-size: 13px; font-weight: 700; }
  .ad-head .arrow { width: 20px; height: 20px; background: var(--arrow-box); display: grid; place-items: center; }

  .ad { margin-bottom: 18px; padding-right: 14px; }
  .ad.gap { margin-top: 30px; }
  .ad-title {
    font-weight: 700; font-size: 15.5px; line-height: 20px;
    color: var(--ad-title); text-decoration: underline; letter-spacing: 0.4px;
  }
  .ad-text { font-size: 14px; line-height: 20.5px; color: var(--ad-text); letter-spacing: 1.1px; }
  .ad-url { font-size: 11.5px; line-height: 16px; color: var(--ad-url); letter-spacing: 0.3px; white-space: nowrap; overflow: hidden; }

  .hero-photo {
    position: absolute; left: 537px; top: 215px; width: 634px; height: 464px;
    background: linear-gradient(90deg, var(--photo-light) 0%, var(--photo-dark) 18%, #3a3c42 50%, var(--photo-dark) 82%, var(--photo-light) 100%);
  }
</style>
</head>
<body>
<div class="page">
  <nav class="main-nav">
    <svg class="home-icon" viewBox="0 0 22 22" aria-hidden="true">
      <rect width="22" height="22" rx="2" fill="#1f9bd7"/>
      <path d="M4 11 L11 5 L18 11 M6.5 10 V17 H9.5 V13 H12.5 V17 H15.5 V10" fill="none" stroke="#fff" stroke-width="2"/>
    </svg>
    <span class="sep">|</span><a href="#">Wichtige regeln</a>
    <span class="sep">|</span><a href="#">Geld sparen</a>
    <span class="sep">|</span><a href="#">Geld verdienen</a>
    <span class="sep">|</span><a href="#">Schuldnerbereatung</a>
    <span class="sep">|</span><a href="#">Impressum</a>
  </nav>

  <div class="brand">finlo-welt</div>

  <aside class="ad-column left">
    <div class="ad-head">
      <span class="source">Plunko<small>-Anzeigen</small></span>
      <span class="arrow"><svg width="10" height="12" viewBox="0 0 10 12"><path d="M2 1 L8 6 L2 11" fill="none" stroke="#fff" stroke-width="2.5"/></svg></span>
    </div>
    <div class="ad">
      <div class="ad-title">1. Kredit-Anfrage in 5min</div>
      <div class="ad-text">2. Angebot in Ruhe prüfen 3. auf Wunsch abschließen</div>
      <div class="ad-url">kreditnest.com/ohneBonvia</div>
    </div>
    <div class="ad">
      <div class="ad-title">Goldene Karte ohne Bonvia</div>
      <div class="ad-text">Echte hochgeprägte Valmora-Karte keine Ablehnung möglich! Sofort</div>
      <div class="ad-url">www.brenkarte-jetzt.eu</div>
    </div>
    <div class="ad gap">
      <div class="ad-title">1. Antrag ausfüllen</div>
      <div class="ad-text">2. Angebot prüfen 3. Schuldenfrei werden</div>
      <div class="ad-url">www.morgen-luftig.com</div>
    </div>
  </aside>

  <aside class="ad-column right">
    <div class="ad-head">
      <span class="source house">finlo-welt</span>
      <span class="arrow"><svg width="10" height="12" viewBox="0 0 10 12"><path d="M2 1 L8 6 L2 11" fill="none" stroke="#fff" stroke-width="2.5"/></svg></span>
    </div>
    <div class="ad">
      <div class="ad-title">1. Antrag ausfüllen</div>
      <div class="ad-text">2. Angebot prüfen 3. Schuldenfrei werden</div>
      <div class="ad-url">www.morgen-luftig.com</div>
    </div>
    <div class="ad gap">
      <div class="ad-title">Billiger Kredit ab 3,45%</div>
      <div class="ad-text">Kredite: für 10.000€ ab 129€/Monat! Alle Kredite kostenlos im Vergleich</div>
      <div class="ad-url">www.Lorvan.de/Kredite-Vergleich</div>
    </div>
    <div class="ad gap">
      <div class="ad-title">Raus aus den Schulden</div>
      <div class="ad-text">Schuldenfrei in 4 Jahren. Sofort Kostenlose Schuldnerberatung</div>
    </div>
  </aside>

  <div class="hero-photo" role="img" aria-label="Mann im dunklen Anzug mit roter Krawatte zieht seine leeren Hosentaschen heraus, Kopf nicht im Bild"></div>
</div>
</body>
</html>
```